Redesign Of Flower Delivery Subscription Service Website

I need a revamped website of www.petal-rush.com

Please revamp current design using same content....

Target Market(s)

people who buy flowers. Brides, wedding planners, wedding photographer, married man, boyfriend, etc.

Industry/Entity Type

Florist

Number of Pages Required

5+ page

Colors

Designer to choose colors to be used in the design.

Requirements
Must have
• I need a revamped website of www.petal-rush.com
• Please revamp current design using same content....
Nice to have
Should not have

```html
<!DOCTYPE html>
<html lang="en">
<head>
<meta charset="utf-8">
<title>Petal Rush – Monthly Flower Delivery</title>
<link href="https://fonts.googleapis.com/css2?family=Great+Vibes&family=Merriweather:wght@400;700&family=Open+Sans:wght@400;600&display=swap" rel="stylesheet">
<style>
:root{
  --green:#8cc63f;
  --green-dark:#79b02f;
  --pink:#f5bfca;
  --pink-soft:#fbe3e8;
  --ink:#2d2d2d;
  --text:#555;
  --dark:#232323;
  --white:#fff;
}
*{box-sizing:border-box;margin:0;padding:0}
html,body{width:1200px;height:3879px;overflow:hidden}
body{font-family:"Open Sans",Arial,sans-serif;color:var(--text);background:var(--white);position:relative}
.abs{position:absolute}
.serif{font-family:"Merriweather",Georgia,serif}
.btn{display:inline-block;background:var(--green);color:var(--white);font-size:15px;font-weight:600;border-radius:24px;text-align:center;width:146px;height:42px;line-height:42px}

/* top bar */
.topbar{left:0;top:0;width:1200px;height:31px;background:var(--dark)}
.social{display:flex;gap:14px;position:absolute;left:132px;top:9px}
.social span{width:13px;height:13px;border-radius:50%;background:var(--white)}
.cart{position:absolute;right:132px;top:7px;color:var(--white);font-size:11px;display:flex;gap:8px;align-items:center}

/* nav */
.nav{left:0;top:31px;width:1200px;height:120px;font-size:12px;color:#444}
.nav-left,.nav-right{position:absolute;top:52px;display:flex;gap:18px;white-space:nowrap}
.nav-left{left:132px}
.nav-right{left:715px}
.logo{position:absolute;left:538px;top:40px;display:flex;align-items:center;gap:8px;font-weight:600;font-size:24px;color:var(--green);white-space:nowrap}
.logo i{width:12px;height:12px;border-radius:50%;background:var(--green)}

/* hero */
.hero{left:0;top:31px;width:1200px;height:672px;background:linear-gradient(90deg,#f4f2f1 0%,#fafafa 45%,#f6f6f6 100%);z-index:-1}
.hero-photo{left:0;top:120px;width:560px;height:583px;background:radial-gradient(ellipse at 45% 45%,#d9c7c2 0%,#ead7da 35%,#f3eeee 70%,rgba(246,246,246,0) 100%)}
.hero-title{left:615px;top:285px;font-family:"Great Vibes",cursive;font-size:96px;font-weight:400;color:var(--ink)}
.hero-sub{left:618px;top:425px;font-size:20px;color:#444;line-height:1.5}
.hero-sub b{color:var(--ink)}
.hero-btn{left:618px;top:512px}

/* features */
.features{left:0;top:703px;width:1200px;height:119px;background:var(--pink);display:flex;justify-content:center;gap:140px;align-items:center}
.feature{display:flex;align-items:center;gap:20px;font-family:"Merriweather",Georgia,serif;font-size:21px;color:var(--ink)}

/* how it works */
.how-photo{left:155px;top:892px;width:427px;height:453px;border-radius:40%;background:radial-gradient(circle at 50% 50%,#f6f0ee 30%,#efc7d0 55%,#d8a9b2 75%,rgba(255,255,255,0) 78%)}
.play{left:340px;top:1059px;width:58px;height:58px}
.tagline{left:615px;top:948px;font-family:"Great Vibes",cursive;font-size:16px;color:var(--green)}
.how-title{left:615px;top:975px;font-size:30px;font-weight:400;color:var(--ink)}
.how-text{left:615px;top:1040px;width:450px;font-size:12.5px;line-height:1.55}
.how-btn{left:615px;top:1240px}

/* email band */
.email-band{left:0;top:1404px;width:1200px;height:473px;background:linear-gradient(180deg,#e88fa1 0%,#f2a9b7 40%,#eb97a8 100%)}
.email-box{left:349px;top:1492px;width:478px;height:292px;background:rgba(255,240,243,.82);padding:38px 32px;text-align:left}
.email-box h2{font-weight:400;font-size:33px;color:#444;line-height:1.35}
.email-box h2 b{font-weight:700}
.field{margin-top:22px;height:50px;border:1px solid #ddd;background:var(--white);font-size:12px;line-height:48px;padding-left:18px;color:#777}
.email-box .btn{display:block;margin:20px auto 0}

/* cards */
.cards-bg{left:0;top:1895px;width:1200px;height:540px;background:linear-gradient(90deg,rgba(248,200,210,.55) 0%,rgba(255,255,255,0) 18%,rgba(255,255,255,0) 82%,rgba(248,200,210,.55) 100%)}
.card{top:1934px;width:295px;height:450px;background:var(--white);box-shadow:0 4px 18px rgba(0,0,0,.1);padding:28px 24px}
.card h3{font-family:"Merriweather",Georgia,serif;font-weight:400;font-size:17px;color:var(--green);text-align:center}
.card .photo{margin-top:22px;height:212px}
.card p{margin-top:26px;font-size:12.5px;line-height:1.55}

/* monthly */
.monthly{left:0;top:2444px;width:1200px;height:1189px;background:linear-gradient(180deg,#f7fbf2 0%,#f6f4f4 60%,#f0eeee 100%)}
.monthly h2{position:absolute;left:0;width:1200px;top:62px;text-align:center;font-size:32px;line-height:1.45;color:var(--ink);font-weight:700}
.row-photo{width:468px;height:310px}
.row-text{width:430px}
.row-text h3{font-family:"Merriweather",Georgia,serif;font-size:21px;line-height:1.4;color:var(--ink)}
.row-text p{margin-top:18px;font-size:12.5px;line-height:1.55}
.row-text .btn{margin-top:22px}

/* footer */
.footer{left:0;top:3633px;width:1200px;height:212px;background:var(--dark);color:var(--white)}
.footer h4{font-family:"Merriweather",Georgia,serif;font-size:21px;font-weight:700}
.contact li{list-style:none;display:flex;gap:18px;align-items:flex-start;font-size:13px;margin-top:14px;line-height:1.45}
.services li{list-style:none;font-size:13px;margin-top:8px;padding-left:18px;position:relative}
.services li::before{content:"";position:absolute;left:0;top:8px;width:4px;height:4px;border-radius:50%;background:#aaa}
.f-field{margin-top:22px;width:295px;height:40px;background:#111;font-size:12px;line-height:40px;padding-left:16px;color:#bbb}
.bottombar{left:0;top:3845px;width:1200px;height:34px;background:#111;color:#ddd;font-size:11px}
</style>
</head>
<body>

<div class="abs topbar">
  <div class="social"><span></span><span></span><span></span><span></span></div>
  <div class="cart">0 items
    <svg width="18" height="14" viewBox="0 0 18 14"><path d="M1 1h3l2 8h9l2-6H5" fill="none" stroke="#fff" stroke-width="1.5"/><circle cx="7" cy="12" r="1.3" fill="#fff"/><circle cx="14" cy="12" r="1.3" fill="#fff"/></svg>
  </div>
</div>

<div class="abs hero"></div>
<div class="abs hero-photo" role="img" aria-label="Pussy willow branches wrapped with a pink satin ribbon on a white table"></div>

<header class="abs nav">
  <nav class="nav-left"><span>Home</span><span>How It Works</span><span>Delivery Areas</span><span>Franchise</span><span>My Account</span></nav>
  <div class="logo"><i></i>Petal Rush</div>
  <nav class="nav-right"><span>Blog</span><span>Free Flowers Monthly</span><span>Corporate Arrangements</span><span>Help</span></nav>
</header>

<h1 class="abs hero-title">Always Fresh</h1>
<p class="abs hero-sub">Beautiful Flower Arrangements Delivered Monthly<br>Now only <b>$69.95/MTH</b> ($100 value)</p>
<a class="abs btn hero-btn">Subscribe</a>

<section class="abs features">
  <div class="feature"><svg width="44" height="48" viewBox="0 0 44 48" fill="none" stroke="#333" stroke-width="2"><circle cx="22" cy="12" r="9"/><path d="M12 22h20l-3 24H15z"/></svg>Free Vase</div>
  <div class="feature"><svg width="48" height="48" viewBox="0 0 48 48" fill="none" stroke="#333" stroke-width="2"><circle cx="24" cy="20" r="14"/><path d="M16 34l8 12 8-12"/></svg>Free Delivery</div>
  <div class="feature"><svg width="50" height="50" viewBox="0 0 50 50" fill="none" stroke="#333" stroke-width="2"><circle cx="25" cy="25" r="22"/><circle cx="25" cy="25" r="10"/></svg>Free Updates</div>
</section>

<div class="abs how-photo" role="img" aria-label="Hand sketching a bouquet, framed by watercolour roses"></div>
<svg class="abs play" viewBox="0 0 58 58" aria-label="Play video"><circle cx="29" cy="29" r="27" fill="rgba(255,255,255,.9)" stroke="#2d2d2d" stroke-width="2"/><path d="M23 18l17 11-17 11z" fill="#2d2d2d"/></svg>
<p class="abs tagline">Fresh Quality Flowers for You</p>
<h2 class="abs how-title serif">How It Works</h2>
<p class="abs how-text">Petal Rush is a SET IT and FORGET IT subscription based flower delivery service. For an amazing price Petal Rush will hand deliver a gorgeous arrangement directly to anyone, anywhere you want, every month.<br>When setting up your account, Petal Rush even lets you choose exact delivery dates for your Anniversary, Birthday, Valentine's and Mother's Day.<br>Our referral program is pretty awesome too! Just refer 3 friends and each month your 3 friends pay to have flowers delivered, your flowers will be delivered free!</p>
<a class="abs btn how-btn">Read More</a>

<section class="abs email-band" role="img" aria-label="Pink painted wooden boards with sprigs of white baby's breath"></section>
<div class="abs email-box">
  <h2 class="serif">Enter Your Email To<br><b>Receive A Free Upgrade !</b></h2>
  <div class="field">Your Email Address</div>
  <a class="btn">Subscribe</a>
</div>

<div class="abs cards-bg" role="img" aria-label="Pink blossom branches at the page edges"></div>
<article class="abs card" style="left:132px">
  <h3>Set It &amp; forget It</h3>
  <div class="photo" role="img" aria-label="Purple and green flower arrangement" style="background:linear-gradient(160deg,#8a5b9a,#5c3a6e 55%,#9fb06a)"></div>
  <p>For an Amazing price Petal Rush will hand deliver a gorgeous arrangement directly to anyone you want every month without you having to worry about it.</p>
</article>
<article class="abs card" style="left:450px">
  <h3>But Never Forget It Again</h3>
  <div class="photo" role="img" aria-label="Cream and blush rose arrangement" style="background:linear-gradient(160deg,#efe3d2,#d9c2a8 55%,#c79a8f)"></div>
  <p>When setting up your account, you can choose exact delivery dates for the months that have special days such as your Anniversary, Birthday, Valentines Day and Mothers Day. You might forget but we won't, we have got ya covered!</p>
</article>
<article class="abs card" style="left:765px">
  <h3>Making someone's day Better</h3>
  <div class="photo" role="img" aria-label="Bouquet of coral roses in a glass vase" style="background:linear-gradient(160deg,#f4eeea,#e77a6e 45%,#6f8f52)"></div>
  <p>Be the hero in that special someone's life each and every month. It feels good to make a difference in your loved ones day.</p>
</article>

<section class="abs monthly" role="img" aria-label="Soft faded pink blossoms in the background">
  <h2 class="serif">Monthly Subscription Based Flower Delivery<br>Service in San Diego — CA by Our Florist Shop</h2>
</section>

<div class="abs row-photo" style="left:132px;top:2630px;background:linear-gradient(150deg,#e9869a,#d65f78 50%,#a9485a)" role="img" aria-label="Large bouquet of pink roses held in hands"></div>
<div class="abs row-text" style="left:628px;top:2680px">
  <h3>Exotic Flowers Garnished With Special Hues To Compliment Your Loved Ones</h3>
  <p>Let's not forget a single day in which you can make your loved ones feel special. Whether it's your anniversary or a birthday in your family, you must always go an extra mile to show "how much I care about you."</p>
  <a class="btn">Read More</a>
</div>

<div class="abs row-photo" style="left:600px;top:2938px;background:linear-gradient(150deg,#1f2230,#3b3a48 45%,#e7b7c8 75%,#f4f0f2)" role="img" aria-label="Bride holding a pink rose bouquet beside a dark suit"></div>
<div class="abs row-text" style="left:158px;top:2995px">
  <h3>Standard And Personalized Flower Arrangements For Special Occasions</h3>
  <p>Petal Rush offers an online subscription based service that is risk free, trouble free and affordable at the same time. We offer the most trusted and delightful flower delivery service in San Diego.</p>
  <a class="btn">Read More</a>
</div>

<div class="abs row-photo" style="left:132px;top:3251px;background:linear-gradient(150deg,#e6e3ea,#8e77c4 45%,#5b3f93)" role="img" aria-label="Purple bellflower bouquet wrapped in satin"></div>
<div class="abs row-text" style="left:635px;top:3300px">
  <h3>Get Yourself Subscribed And Claim Discounts On Big Orders!</h3>
  <p>Get love and adulation by gifting flowers to your loved ones on those special occasions. Whether it's formal, personal or your love for your family, just follow the subscription criteria and get your hands on the most valuable service.</p>
  <a class="btn">Read More</a>
</div>

<footer class="abs footer">
  <div class="abs contact" style="left:132px;top:28px">
    <h4>Contact Info</h4>
    <ul>
      <li><svg width="14" height="18" viewBox="0 0 14 18"><path d="M7 1a6 6 0 0 0-6 6c0 4.5 6 10 6 10s6-5.5 6-10a6 6 0 0 0-6-6z" fill="#fff"/><circle cx="7" cy="7" r="2.2" fill="#232323"/></svg><span>418 Juniper Row,<br>Lemon Grove, CA 91945</span></li>
      <li><svg width="16" height="12" viewBox="0 0 16 12"><rect x="0.5" y="0.5" width="15" height="11" fill="#fff"/><path d="M1 1l7 6 7-6" fill="none" stroke="#232323"/></svg><span>hello@petalrushsd.com</span></li>
      <li><svg width="15" height="15" viewBox="0 0 15 15"><path d="M3 1l3 3-2 2c1 2 3 4 5 5l2-2 3 3-2 2C7 14 1 8 1 3z" fill="#fff"/></svg><span>555-014-2288</span></li>
    </ul>
  </div>
  <div class="abs services" style="left:478px;top:28px">
    <h4>More Services</h4>
    <ul style="margin-top:14px">
      <li>Corporate Arrangements</li><li>Hotel Arrangements</li><li>Events</li><li>Weddings</li>
    </ul>
  </div>
  <div class="abs" style="left:775px;top:28px">
    <h4>Recieve a Free Upgrade</h4>
    <div class="f-field">Your Email Address</div>
    <a class="btn" style="margin:10px 0 0 150px">Subscribe</a>
  </div>
</footer>
<div class="abs bottombar">
  <span class="abs" style="left:132px;top:11px">Petal Rush - Monthly Flowers Delivery Copyright 2018. All Rights Reserved.</span>
  <span class="abs" style="right:132px;top:11px">Privacy Policy Terms &amp; Conditions</span>
</div>

</body>
</html>
```